Logo and Business card design!

Welbrook Estates

We are a Property development and real estate company (needs a logo design).

Welbrook estates is based in Sydney Australia and will be dealing with high net worth individuals with a corporate background. The demographic of clients will be relatively youthful and savvy. We do development finance, property development and some portion of property sales

I'd like the 'Welbrook' part of the name to be strength of the title, with 'property' playing a very minor part, perhaps in tiny font somewhere off to the bottom or side or something

Thank you!

Target Market(s)

25-55 years old

Industry/Entity Type

Real Estate Development

Contact Information for Business Card

Please arrange this information as you see fit

Leon Brightwater
Managing Director
0417 582 273
leon@welbrookestates-example.com.au
www.welbrookestates-example.com.au

Logo Text

Welbrook estates

Font styles to use
Serif

Colors

Designer to choose colors to be used in the design.

Requirements
Must have
• PLEASE VIEW THE UPLOADED IMAGES AND EXAMPLES
• And please put 'property' in small letters at the bottom or to the side. I want it to play a minimalist role, with 'WELBROOK' being the feature
• Colours! Please make sure theyre mostly grey and white with possibly some other dark blue and maybe dark grey
Nice to have
• Please feel free to use whatever colors you like, the suggested colors are something I selected momentarily and dont necessarily reflect strict guidelines
Should not have
• NO pictures or shapes of houses. I dont want the logo design to be so literal in its imagery

```html
<!DOCTYPE html>
<html lang="en">
<head>
<meta charset="utf-8">
<title>Welbrook Estates – Business Card</title>
<link rel="stylesheet" href="https://fonts.googleapis.com/css2?family=Noto+Serif:wght@400&family=Open+Sans:wght@400;600&display=swap">
<style>
  :root {
    --page: #ffffff;
    --card-dark: #000000;
    --card-light: #ffffff;
    --ink-light: #ffffff;
    --ink-dark: #111111;
    --accent: #2b2350;
    --shadow: rgba(0, 0, 0, 0.45);
  }
  * { margin: 0; padding: 0; box-sizing: border-box; }
  html, body {
    width: 1200px;
    height: 1200px;
    overflow: hidden;
    background: var(--page);
  }
  .sheet { position: relative; width: 1200px; height: 1200px; }

  .card {
    position: absolute;
    left: 170px;
    width: 868px;
    height: 528px;
    box-shadow: 10px 12px 14px var(--shadow);
  }
  .card--front { top: 64px; background: var(--card-dark); }
  .card--back { top: 602px; background: var(--card-light); display: flex; }

  .brand {
    position: absolute;
    left: 0;
    right: 0;
    text-align: center;
    color: var(--ink-light);
    font-family: "Noto Serif", Georgia, serif;
    font-weight: 400;
  }
  .brand__mark {
    display: block;
    margin: 0 auto;
    background: var(--ink-light);
  }
  .brand__name { display: block; line-height: 1; }
  .brand__tag { display: block; line-height: 1; }

  .card--front .brand { top: 106px; }
  .card--front .brand__mark { width: 70px; height: 70px; }
  .card--front .brand__name { font-size: 112px; margin-top: 50px; letter-spacing: 2px; }
  .card--front .brand__tag { font-size: 32px; margin-top: 58px; letter-spacing: 64px; margin-right: -64px; }

  .back__logo-side {
    position: relative;
    width: 473px;
    height: 100%;
    background: var(--card-dark);
  }
  .back__logo-side .brand { top: 146px; }
  .back__logo-side .brand__mark { width: 48px; height: 48px; }
  .back__logo-side .brand__name { font-size: 74px; margin-top: 46px; letter-spacing: 1px; }
  .back__logo-side .brand__tag { font-size: 22px; margin-top: 32px; letter-spacing: 44px; margin-right: -44px; }

  .contact {
    flex: 1;
    text-align: center;
    color: var(--ink-dark);
    font-family: "Open Sans", Arial, sans-serif;
    padding-top: 116px;
  }
  .contact__name {
    font-family: "Noto Serif", Georgia, serif;
    font-size: 39px;
    font-weight: 400;
    color: var(--accent);
    line-height: 1.1;
  }
  .contact__role {
    font-size: 17px;
    font-weight: 600;
    letter-spacing: 3.6px;
    margin-top: 8px;
  }
  .contact__icon { display: block; margin: 0 auto; fill: var(--accent); }
  .contact__icon--phone { margin-top: 56px; }
  .contact__icon--mail { margin-top: 18px; }
  .contact__line { font-size: 18px; line-height: 1.5; }
  .contact__line--phone { margin-top: 6px; }
  .contact__line--email { margin-top: 8px; font-size: 17px; }
  .contact__line--web { font-size: 17px; }
</style>
</head>
<body>
<div class="sheet">

  <section class="card card--front">
    <div class="brand">
      <span class="brand__mark"></span>
      <span class="brand__name">WELBROOK</span>
      <span class="brand__tag">ESTATES</span>
    </div>
  </section>

  <section class="card card--back">
    <div class="back__logo-side">
      <div class="brand">
        <span class="brand__mark"></span>
        <span class="brand__name">WELBROOK</span>
        <span class="brand__tag">ESTATES</span>
      </div>
    </div>

    <div class="contact">
      <h1 class="contact__name">Leon Brightwater</h1>
      <p class="contact__role">Managing Director</p>

      <svg class="contact__icon contact__icon--phone" width="36" height="34" viewBox="0 0 36 34" aria-hidden="true">
        <path d="M4 30 C1 24 2 12 12 5 C20 0 30 1 34 5 L30 11 C27 9 23 8 19 10 L21 15 C16 17 12 22 11 27 L6 27 Z"/>
      </svg>
      <p class="contact__line contact__line--phone">0417 582 273</p>

      <svg class="contact__icon contact__icon--mail" width="38" height="28" viewBox="0 0 38 28" aria-hidden="true">
        <path d="M0 0 H38 V28 H0 Z M4 4 V24 H34 V4 Z"/>
        <path d="M4 4 L19 16 L34 4" fill="none" stroke="var(--accent)" stroke-width="4"/>
      </svg>
      <p class="contact__line contact__line--email">leon@welbrookestates-example.com.au</p>
      <p class="contact__line contact__line--web">www.welbrookestates-example.com.au</p>
    </div>
  </section>

</div>
</body>
</html>
```